Road Construction Company needs business cards

We would like a new business card designed for our business.

We're a road construction company based in Qld, Australia.

Can the business card please have the following information on it.

Name: Brent Malvoy
Position: General Manager
Phone: 0471 592 304
Email: Brent.malvoy@quendix.com.au
Address: 87 Harrowgate Ave, Pindarra, QLD, 4000
Website: www.quendix.com.au

Visually we'd like the card to be professional and simple.

Attached is our logo.

Our website is www.quendix.com.au

Target Market(s)

Men aged 25-60

Contact Information for Business Card

As listed in project description

Font styles to use
Serif

Requirements
Must have
• Large logo on back of card

```html
<!DOCTYPE html>
<html lang="en">
<head>
<meta charset="UTF-8">
<title>Quendix Road Construction – Business Card</title>
<link rel="stylesheet" href="https://fonts.googleapis.com/css2?family=Roboto+Slab:wght@400;700;800&display=swap">
<style>
  :root {
    --canvas-bg: #e9ebee;
    --card-white: #ffffff;
    --brand-navy: #0d4ea6;
    --brand-deep: #0a3f8f;
    --brand-sky: #2fa2dc;
    --text-grey: #55595f;
    --divider: #1c5fb4;
    --photo-top: #7f93a6;
    --photo-bottom: #2b2e37;
    --white: #ffffff;
  }
  * { box-sizing: border-box; margin: 0; padding: 0; }
  html, body { width: 1200px; height: 900px; overflow: hidden; }
  body {
    background: var(--canvas-bg);
    font-family: "Roboto Slab", serif;
    position: relative;
  }
  .card {
    position: absolute;
    left: 250px;
    width: 700px;
    height: 400px;
    border-radius: 16px;
    overflow: hidden;
    box-shadow: 0 10px 30px rgba(0,0,0,.18);
  }
  .card--front { top: 36px; background: var(--card-white); }
  .card--back { top: 466px; }

  /* Front */
  .front-swoosh { position: absolute; inset: 0; width: 100%; height: 100%; }
  .front-brand {
    position: absolute;
    left: 48px;
    top: 118px;
    color: var(--brand-navy);
    font-weight: 800;
    line-height: 1;
  }
  .front-brand__name { font-size: 58px; letter-spacing: -1px; display: block; }
  .front-brand__tag {
    font-size: 13px;
    letter-spacing: 6.5px;
    display: block;
    margin-top: 8px;
  }
  .front-divider {
    position: absolute;
    left: 372px;
    top: 118px;
    width: 1.5px;
    height: 200px;
    background: var(--divider);
  }
  .contact { position: absolute; left: 390px; top: 112px; color: var(--text-grey); }
  .contact__name {
    font-size: 26px;
    font-weight: 700;
    color: var(--brand-navy);
    text-transform: uppercase;
    line-height: 1.1;
  }
  .contact__role {
    font-size: 14px;
    text-transform: uppercase;
    letter-spacing: .8px;
    margin-bottom: 10px;
  }
  .contact__address { font-size: 15px; line-height: 1.35; margin-bottom: 6px; }
  .contact__list { list-style: none; font-size: 14px; line-height: 1.6; }
  .contact__list li { display: flex; align-items: center; gap: 7px; }
  .contact__icon { width: 12px; height: 12px; flex: none; }

  /* Back */
  .back-photo {
    position: absolute;
    inset: 0;
    background: linear-gradient(180deg, var(--photo-top) 0%, var(--photo-bottom) 100%);
  }
  .back-brand {
    position: absolute;
    left: 0; right: 0;
    top: 200px;
    text-align: center;
    color: var(--white);
    font-weight: 800;
    line-height: 1;
  }
  .back-brand__name { display: block; font-size: 80px; letter-spacing: -1px; }
  .back-brand__tag { display: block; font-size: 18px; letter-spacing: 10px; margin-top: 12px; }
</style>
</head>
<body>

<section class="card card--front" aria-label="Business card front">
  <svg class="front-swoosh" viewBox="0 0 700 400" preserveAspectRatio="none" aria-hidden="true">
    <path d="M0,262 C110,330 330,372 700,362 L700,400 L0,400 Z" fill="var(--brand-deep)"/>
    <path d="M150,300 C300,355 480,368 700,348" fill="none" stroke="var(--card-white)" stroke-width="7"/>
    <path d="M150,300 C300,355 480,368 700,348" fill="none" stroke="var(--brand-sky)" stroke-width="4"/>
  </svg>

  <div class="front-brand">
    <span class="front-brand__name">QUENDIX</span>
    <span class="front-brand__tag">ROAD CONSTRUCTION</span>
  </div>

  <div class="front-divider"></div>

  <div class="contact">
    <h1 class="contact__name">Brent Malvoy</h1>
    <p class="contact__role">General Manager</p>
    <p class="contact__address">87 Harrowgate Ave,<br>Pindarra, QLD, 4000</p>
    <ul class="contact__list">
      <li>
        <svg class="contact__icon" viewBox="0 0 12 12" aria-hidden="true"><path d="M3 1 L5 3.5 L4 5 C4.8 6.6 5.6 7.4 7 8 L8.5 7 L11 9 L9.5 11 C5 10.5 1.5 7 1 2.5 Z" fill="var(--brand-navy)"/></svg>
        0471 592 304
      </li>
      <li>
        <svg class="contact__icon" viewBox="0 0 12 12" aria-hidden="true"><rect x="1" y="2.5" width="10" height="7" fill="none" stroke="var(--brand-navy)" stroke-width="1.2"/><path d="M1 2.5 L6 6.5 L11 2.5" fill="none" stroke="var(--brand-navy)" stroke-width="1.2"/></svg>
        Brent.malvoy@quendix.com.au
      </li>
      <li>
        <svg class="contact__icon" viewBox="0 0 12 12" aria-hidden="true"><circle cx="6" cy="6" r="5" fill="none" stroke="var(--brand-navy)" stroke-width="1.1"/><ellipse cx="6" cy="6" rx="2.2" ry="5" fill="none" stroke="var(--brand-navy)" stroke-width="1"/><path d="M1 6 H11" stroke="var(--brand-navy)" stroke-width="1"/></svg>
        www.quendix.com.au
      </li>
    </ul>
  </div>
</section>

<section class="card card--back" aria-label="Business card back">
  <div class="back-photo" role="img" aria-label="Photo of a road crew in high-visibility workwear beside an asphalt paver on a freshly laid street"></div>
  <div class="back-brand">
    <span class="back-brand__name">QUENDIX</span>
    <span class="back-brand__tag">ROAD CONSTRUCTION</span>
  </div>
</section>

</body>
</html>
```